Night Dresses business cards business requirers

We are a new company initiating Mexico operations. Our core business is Night woman dress (both formal and party dress) for rent. Gownhaven is the name of the company. ITS Gownhaven form by two word. The dress word and topia (Utopic) so the place Gownhaven Means That You cant get the ideal, perfect and unique dress for your event. So we would like a modern, very creative, and attractive business card.

Industry/Entity Type

Womens Clothing

Contact Information for Business Card

Rounded Borders, two faces

Requirements
Must have
• Rounded borders, logo and slogan, modern, glam, attractive design
Should not have
• modern design classic or not

```html
<!DOCTYPE html>
<html lang="en">
<head>
<meta charset="utf-8">
<title>Gownhaven business cards</title>
<link href="https://fonts.googleapis.com/css2?family=Source+Sans+3:wght@400;600&display=swap" rel="stylesheet">
<style>
  :root {
    --backdrop: #5a4838;
    --card: #ffffff;
    --orchid: #b5609a;
    --ink: #4a4a4a;
    --brand-grey: #5c5c5c;
  }
  * { margin: 0; padding: 0; box-sizing: border-box; }
  html, body {
    width: 1200px; height: 987px; overflow: hidden;
    background: var(--backdrop);
    font-family: "Source Sans 3", "Myriad Pro", sans-serif;
  }
  .canvas { position: relative; width: 1200px; height: 987px; }
  .card {
    position: absolute; left: 293px; width: 615px; height: 352px;
    background: var(--card); border-radius: 22px; overflow: hidden;
    box-shadow: 0 3px 6px rgba(0,0,0,0.35);
  }
  .card--front { top: 130px; }
  .card--back { top: 505px; }

  .holder { position: absolute; left: 39px; top: 38px; }
  .holder__name { color: var(--orchid); font-size: 21px; font-weight: 600; line-height: 1.1; }
  .holder__role { color: var(--ink); font-size: 16px; margin-top: 3px; }

  .address { position: absolute; left: 39px; top: 98px; color: var(--ink); font-size: 16px; line-height: 22px; }

  .contacts { position: absolute; left: 39px; top: 146px; list-style: none; }
  .contacts li { display: flex; align-items: center; height: 23.4px; color: var(--ink); font-size: 16px; }
  .contacts svg { width: 15px; height: 15px; margin-right: 9px; fill: var(--orchid); flex: none; }

  .company-name { color: var(--brand-grey); font-weight: 400; line-height: 1; }

  .brand-front { position: absolute; left: 39px; top: 284px; }
  .brand-front .company-name { font-size: 26px; }

  .emblem-large {
    position: absolute; left: 282px; top: 17px; width: 316px; height: 316px;
    border: 5px solid var(--orchid); border-radius: 50%;
  }

  .brand-back { position: absolute; left: 0; right: 0; top: 76px; display: flex; flex-direction: column; align-items: center; }
  .emblem-small { width: 108px; height: 108px; border: 3px solid var(--orchid); border-radius: 50%; }
  .brand-back .company-name { margin-top: 16px; font-size: 30px; }
</style>
</head>
<body>
<main class="canvas">
  <section class="card card--front" aria-label="Card front">
    <div class="holder">
      <p class="holder__name">ELENA MARQUEZ</p>
      <p class="holder__role">CEO/Founder</p>
    </div>
    <p class="address">214 Jacaranda Court<br>Guadalajara, Jalisco 44100</p>
    <ul class="contacts">
      <li><svg viewBox="0 0 16 16" aria-hidden="true"><path d="M3.5 1l2.5 3-1.5 2a9 9 0 0 0 5 5l2-1.5 3 2.5-1.5 2.5C7 14.5 1.5 9 1 3z"/></svg>331 502 7846</li>
      <li><svg viewBox="0 0 16 16" aria-hidden="true"><path d="M4.5 0h7a1 1 0 0 1 1 1v14a1 1 0 0 1-1 1h-7a1 1 0 0 1-1-1V1a1 1 0 0 1 1-1zm.8 2v10.5h5.4V2zM8 13.3a.9.9 0 1 0 0 1.8.9.9 0 0 0 0-1.8z"/></svg>331 918 4027</li>
      <li><svg viewBox="0 0 16 16" aria-hidden="true"><path d="M4 1h8v4H4zM1 6h14v6h-2.5v-2h-9v2H1zM4.5 11h7v4h-7z"/></svg>331 264 5193</li>
      <li><svg viewBox="0 0 16 16" aria-hidden="true"><path d="M1 3h14v1.2L8 9 1 4.2zM1 5.8l7 4.8 7-4.8V13H1z"/></svg>hello@gownhaven.mx</li>
      <li><svg viewBox="0 0 16 16" aria-hidden="true"><path d="M8 1a7 7 0 1 0 0 14A7 7 0 0 0 8 1zm-1 2.2c-.5 1-2.6 1.3-2.4 2.8.2 1.3 2 .9 2.4 2.2.4 1.2-.8 2 .2 3.6-2.5-.4-4.4-2.6-4.4-5.3A5.3 5.3 0 0 1 7 3.2zm3 .3a5.3 5.3 0 0 1 2.8 6.6c-.9-.6-.6-2-1.7-2.3-1-.3-1.7.6-2.3-.2-.5-.8.8-1.5.6-2.4-.1-.8-.1-1.2.6-1.7z"/></svg>www.gownhaven.mx</li>
    </ul>
    <div class="brand-front">
      <p class="company-name">Gownhaven</p>
    </div>
    <div class="emblem-large" aria-hidden="true"></div>
  </section>

  <section class="card card--back" aria-label="Card back">
    <div class="brand-back">
      <div class="emblem-small" aria-hidden="true"></div>
      <p class="company-name">Gownhaven</p>
    </div>
  </section>
</main>
</body>
</html>
```